PSD website for property company

Please read the brief thoroughly.

We are looking for a new website for a property group that does property acquisitions, property development and property management.
They buy, build and lease core inner city industrial assets in Sydney, Australia.
They also invest in residential developments.

Site menu
- Home page
- Property – sub menus include – Leasing ; Projects ; Investments ; Property Management
- Capital and finance
- About
- Contact

They like this website
https://www.verlo.com.au/

They want the site to be clean, modern and bold.
They like few colors, even black and white is OK to submit

They have a logo and style guide and useable images here:
http://www.kumet.net/temp/PelorisWeb2019.zip
The zip file is also attached to this project.
We have supplied some images to give you an idea, but we will also require you to provide at least 3 extra images from stock photos.
Use your imagination.

I am expecting a lot of similar designs, so be aware the photos you choose will be really important.
They want really 3 good stock photos used and supplied without charge.
Please not too generic, I repeat the quality of the photos is important.
You may provide several photos (but not in multiple submissions please) and we will choose the best three to be provided.

The winner will be selected on a single home page design and required to provide;
All photos use in original format without charge
A second ‘standard page’ template design based on the winning home page design

```html
<!DOCTYPE html>
<html lang="en">
<head>
<meta charset="utf-8">
<title>Peloris — Property Group</title>
<link rel="stylesheet" href="https://fonts.googleapis.com/css2?family=Anton&family=Arimo:wght@400;700&display=swap">
<style>
  :root{
    --green-dark:#546b30;
    --green-sage:#8fa78c;
    --green-line:#a8bca5;
    --white:#ffffff;
    --ink:#333333;
    --footer:#2b2b2b;
    --footer-text:#d8d8d8;
  }
  *{margin:0;padding:0;box-sizing:border-box}
  html,body{width:1200px;height:2317px;overflow:hidden;background:var(--white)}
  body{position:relative;font-family:"Arimo",Arial,sans-serif;color:var(--ink)}
  .abs{position:absolute}

  /* Navigation */
  .site-nav{position:absolute;left:0;top:0;width:1200px;height:79px;background:var(--green-dark)}
  .nav-link{position:absolute;top:31px;font-size:14.5px;color:var(--white);white-space:nowrap}
  .nav-link svg{vertical-align:middle;margin-left:4px}
  .brand{position:absolute;top:22px;left:0;width:1200px;text-align:center;font-weight:700;font-size:33px;letter-spacing:12px;color:var(--white);padding-left:12px;line-height:1}

  /* Hero */
  .hero{position:absolute;left:0;top:79px;width:1200px;height:596px}
  .hero-photo{position:absolute;inset:0;background:linear-gradient(180deg,#4b4a45 0%,#3e3b35 40%,#3a3834 70%,#4a4a48 100%)}
  .hero-shade{position:absolute;inset:0;background:radial-gradient(ellipse at 50% 45%,rgba(110,90,70,.35),rgba(30,30,30,.2) 70%)}
  .hero-bar{position:absolute;top:81px;width:9px;height:434px;background:var(--white)}
  .hero-title{position:absolute;top:226px;left:0;width:1200px;text-align:center;font-family:"Anton",Impact,sans-serif;font-size:53px;color:var(--white);letter-spacing:1px;line-height:1.1}
  .hero-cta{position:absolute;left:463px;top:311px;width:275px;height:72px;border-radius:36px;background:var(--green-sage);color:var(--white);font-weight:700;font-size:14px;display:flex;align-items:center;justify-content:center;letter-spacing:.3px}
  .scroll-cue{position:absolute;left:0;top:523px;width:1200px;text-align:center;color:#cfcfcf;font-weight:700;font-size:14px;letter-spacing:.5px}
  .scroll-line{position:absolute;left:598px;top:546px;width:4px;height:41px;background:#9a9a9a}
  .side-tab{position:absolute;left:1108px;top:81px}
  .side-label{position:absolute;color:var(--white);font-weight:700;font-size:12px;transform:rotate(-90deg);transform-origin:left top;white-space:nowrap;letter-spacing:.3px}

  /* Welcome */
  .rule-v{position:absolute;width:6px;background:var(--green-line)}
  .rule-h{position:absolute;height:6px;background:var(--green-line)}
  .section-title{position:absolute;font-family:"Anton",Impact,sans-serif;font-size:30px;line-height:36px;color:var(--green-dark);letter-spacing:.5px}
  .body-copy{position:absolute;font-size:14.2px;line-height:24.7px;color:var(--ink);text-align:justify}
  .photo{position:absolute}

  /* Projects */
  .slider-btn{position:absolute;top:1661px;width:40px;height:40px;border:2px solid var(--green-dark);display:flex;align-items:center;justify-content:center}
  .slider-btn.is-active{background:var(--green-dark)}
  .project-card{position:absolute;top:1715px;width:283px;height:369px;overflow:hidden}
  .project-card .card-shade{position:absolute;left:0;right:0;bottom:0;height:120px;background:linear-gradient(180deg,rgba(0,0,0,0),rgba(0,0,0,.55))}
  .card-caption{position:absolute;left:38px;top:304px;color:var(--white)}
  .card-caption::before{content:"";position:absolute;left:-15px;top:4px;width:6px;height:34px;background:var(--white)}
  .card-title{font-weight:700;font-size:15px;line-height:19px}
  .card-sub{font-size:12.5px;line-height:20px}

  /* Footer */
  .site-footer{position:absolute;left:0;top:2133px;width:1200px;height:184px;background:var(--footer)}
  .footer-brand{position:absolute;left:169px;top:70px;font-weight:700;font-size:46px;letter-spacing:17px;color:var(--white);line-height:1}
  .footer-heading{position:absolute;top:25px;font-weight:700;font-size:14.5px;color:var(--white)}
  .footer-list{position:absolute;top:60px;list-style:none;font-size:12.5px;color:var(--footer-text)}
  .footer-list li{height:27px}
</style>
</head>
<body>

<header class="site-nav">
  <span class="nav-link" style="left:179px">Capital and Finace</span>
  <span class="nav-link" style="left:367px">Property<svg width="10" height="7" viewBox="0 0 10 7"><path d="M1 1.5l4 3.5 4-3.5" fill="none" stroke="#fff" stroke-width="2"/></svg></span>
  <div class="brand">PELORIS</div>
  <span class="nav-link" style="left:762px">About Us</span>
  <span class="nav-link" style="left:908px">Contact Us</span>
</header>

<section class="hero">
  <div class="hero-photo" role="img" aria-label="Dusk view of a brick mid-rise building with arched ground-floor shopfronts and street trees"></div>
  <div class="hero-shade"></div>
  <div class="hero-bar" style="left:169px"></div>
  <div class="hero-bar" style="left:1021px"></div>
  <h1 class="hero-title">LOVE THIS PROPERTY</h1>
  <div class="hero-cta">COMING SOON...</div>
  <div class="scroll-cue">SCROLL</div>
  <div class="scroll-line"></div>

  <div class="side-tab">
    <svg width="92" height="434" viewBox="0 0 92 434">
      <polygon points="92,0 92,434 0,348 0,86" fill="#8fa78c"/>
      <g fill="#fff">
        <rect x="33" y="150" width="10" height="22"/>
        <rect x="45" y="156" width="12" height="16"/>
        <line x1="46" y1="197" x2="46" y2="238" stroke="#fff" stroke-width="1.5"/>
        <rect x="33" y="262" width="26" height="19" rx="1"/>
      </g>
      <g fill="#8fa78c">
        <rect x="35" y="154" width="2.5" height="2.5"/><rect x="39" y="154" width="2.5" height="2.5"/>
        <rect x="35" y="160" width="2.5" height="2.5"/><rect x="39" y="160" width="2.5" height="2.5"/>
        <rect x="47" y="159" width="8" height="2"/><rect x="47" y="164" width="8" height="2"/>
      </g>
      <path d="M33 263l13 10 13-10" fill="none" stroke="#8fa78c" stroke-width="1.8"/>
    </svg>
    <span class="side-label" style="left:37px;top:132px">PROPERTY</span>
    <span class="side-label" style="left:37px;top:351px">ENQUIRY</span>
  </div>
</section>

<section class="welcome">
  <div class="rule-v" style="left:169px;top:742px;height:478px"></div>
  <h2 class="section-title" style="left:216px;top:736px">WELCOME TO<br>PELORIS</h2>
  <p class="body-copy" style="left:216px;top:829px;width:340px">Lorem ipsum dolor sit amet, consectetur adipiscing elit. Donec ultrices sit amet quam eget euismod. Nulla et ullamcorper libero. Etiam neque urna, tincidunt semper massa ut facilisis ultrices nunc. Integer ut magna a erat placerat tincidunt at eget augue. Nam sit amet lobortis ipsum. Aliquam erat volutpat. Morbi auctor dui quam, sed interdum sem mollis nec. Integer tempus bibendum lacinia. Nullam convallis ipsum eu molestie maximus.</p>
  <div class="photo" style="left:642px;top:741px;width:389px;height:490px;background:linear-gradient(180deg,#b9c8d3 0%,#a99b86 35%,#6e5a45 70%,#5b4a3a 100%)" role="img" aria-label="Brick townhouse facade with a large white arched window and arched ground-floor openings"></div>
  <div class="photo" style="left:102px;top:1121px;width:418px;height:267px;background:linear-gradient(180deg,#c7d5df 0%,#cfcac4 40%,#a49a8f 70%,#7f8a56 100%)" role="img" aria-label="Pale concrete building with arched colonnade beside a grassy park"></div>
  <div class="rule-h" style="left:117px;top:1164px;width:603px"></div>
</section>

<section class="projects">
  <div class="photo" style="left:314px;top:1429px;width:277px;height:200px;background:linear-gradient(135deg,#3d9ad6 0%,#7cc0e6 35%,#c9a24a 65%,#2a6f9a 100%)" role="img" aria-label="Building under construction with yellow and blue facade panels against a blue sky"></div>
  <h2 class="section-title" style="left:693px;top:1446px;width:296px;text-align:right">EXPLORE OUR<br>LATEST PROJECTS</h2>
  <p class="body-copy" style="left:693px;top:1542px;width:296px;text-align:right">Lorem ipsum dolor sit amet, consectetur adipiscing elit. Donec ultrices sit amet quam eget euismod. Nulla et ullamcorper libero.</p>
  <div class="rule-v" style="left:1025px;top:1453px;height:329px"></div>
  <div class="rule-h" style="left:470px;top:1666px;width:609px"></div>

  <div class="slider-btn is-active" style="left:169px"><svg width="10" height="14" viewBox="0 0 10 14"><path d="M8 2L3 7l5 5" fill="none" stroke="#fff" stroke-width="2.5"/></svg></div>
  <div class="slider-btn" style="left:213px"><svg width="10" height="14" viewBox="0 0 10 14"><path d="M2 2l5 5-5 5" fill="none" stroke="#546b30" stroke-width="2.5"/></svg></div>

  <article class="project-card" style="left:130px">
    <div class="photo" style="inset:0;background:linear-gradient(170deg,#4a94e0 0%,#3d6fb8 35%,#7a3550 70%,#4a0f14 100%)" role="img" aria-label="Corner of a glass tower with red vertical fins against blue sky"></div>
    <div class="card-shade"></div>
    <div class="card-caption"><div class="card-title">Lorem ipsum dolor</div><div class="card-sub">sitamet, consec</div></div>
  </article>
  <article class="project-card" style="left:458px">
    <div class="photo" style="inset:0;background:linear-gradient(90deg,#6f6e6a 0%,#8a8a86 45%,#b8282a 70%,#c42a2c 100%)" role="img" aria-label="Grey apartment facade with tall windows beside a red panelled wall"></div>
    <div class="card-shade"></div>
    <div class="card-caption"><div class="card-title">Lorem ipsum dolor</div><div class="card-sub">sitamet, consec</div></div>
  </article>
  <article class="project-card" style="left:784px">
    <div class="photo" style="inset:0;background:linear-gradient(180deg,#9a9a98 0%,#5d5b58 45%,#3b3937 75%,#4e4b48 100%)" role="img" aria-label="Timber-clad grey building with red window shutters"></div>
    <div class="card-shade"></div>
    <div class="card-caption"><div class="card-title">Lorem ipsum dolor</div><div class="card-sub">sitamet, consec</div></div>
  </article>
</section>

<footer class="site-footer">
  <div class="footer-brand">PELORIS</div>
  <div class="footer-heading" style="left:677px">Company</div>
  <ul class="footer-list" style="left:677px">
    <li>Property</li><li>Capital and finance</li><li>About</li><li>Contact</li>
  </ul>
  <div class="footer-heading" style="left:862px">Get in touch</div>
  <ul class="footer-list" style="left:862px">
    <li>(000) 000-000-000</li><li>example@example.com</li>
  </ul>
</footer>

</body>
</html>
```